We sell companies excess stock for them

We need a business card for a company based in New Zealand called 'StockHarbor'.

Check out our website to get an idea www.stockharbor.example

We help other businesses to;
- Sell Excess Stock
- Manage Product Returns
- Sell Company Assets

Our logo is attached for your reference
The font used is 'RifficFree-Bold'

Target Market(s)

Businesses

Industry/Entity Type

Business

Contact Information for Business Card

Name: Mark Pellow
Phone: 027 846 2093
email: markpellow@stockharbor.example
website: www.stockharbor.example

Font styles to use
Other font styles liked:
• Unsure

Colors
9bcb3b

Requirements
Must have
• coming soon
Nice to have
• coming soon
Should not have
• coming soon

```html
<!DOCTYPE html>
<html lang="en">
<head>
<meta charset="UTF-8">
<title>StockHarbor Business Card</title>
<link href="https://fonts.googleapis.com/css2?family=Lato:wght@400;700&display=swap" rel="stylesheet">
<style>
  :root {
    --backdrop: #3a302c;
    --card-white: #f6f6f4;
    --card-black: #0d0d0d;
    --ink: #231f20;
    --ink-soft: #3c3c3c;
    --brand-green: #9bcb3b;
    --rule: #cfcfcf;
  }
  * { margin: 0; padding: 0; box-sizing: border-box; }
  html, body {
    width: 1200px; height: 900px; overflow: hidden;
    background: var(--backdrop);
    font-family: "Lato", sans-serif;
  }
  .stage {
    position: relative; width: 1200px; height: 900px;
    display: flex; align-items: center; justify-content: center; gap: 40px;
  }
  .card {
    position: relative; width: 540px; height: 310px;
    box-shadow: 0 12px 30px rgba(0,0,0,0.35);
  }
  .card-front { background: var(--card-white); color: var(--ink); }
  .card-back { background: var(--card-black); }

  .brand-name {
    position: absolute; right: 34px; top: 62px;
    font-weight: 700; font-size: 46px; letter-spacing: -1px;
    color: var(--ink);
  }
  .divider {
    position: absolute; left: 150px; right: 26px; top: 140px;
    height: 1px; background: var(--rule);
  }
  .services {
    position: absolute; right: 30px; top: 154px;
    list-style: none; text-align: right;
    font-size: 15px; line-height: 19px; color: var(--ink-soft);
  }
  .services li::after {
    content: ""; display: inline-block; width: 8px; height: 8px;
    margin-left: 6px; border-radius: 50%; background: var(--ink);
    vertical-align: 1px;
  }
  .contact {
    position: absolute; left: 32px; bottom: 30px;
  }
  .person-name {
    font-size: 26px; font-weight: 700; color: var(--ink);
    margin-bottom: 8px;
  }
  .person-name .surname { color: var(--brand-green); }
  .contact-list { list-style: none; font-size: 16px; line-height: 22px; color: var(--ink-soft); }
  .contact-list li { display: flex; align-items: center; gap: 8px; }
  .contact-list svg { width: 13px; height: 13px; fill: var(--brand-green); flex: none; }

  .mascot-art {
    position: absolute; left: 50%; top: 40px; width: 190px; height: 150px;
    transform: translateX(-50%);
    border-radius: 40px;
    background: radial-gradient(circle at 50% 45%, #f2a03a 0%, #7bb33a 55%, #2a2a2a 100%);
  }
  .back-url {
    position: absolute; left: 0; right: 0; top: 222px; text-align: center;
    font-size: 17px; font-weight: 700; letter-spacing: 3px;
    color: var(--brand-green);
  }
</style>
</head>
<body>
<main class="stage">
  <section class="card card-front">
    <div class="brand-name">StockHarbor</div>
    <div class="divider"></div>
    <ul class="services">
      <li>Sell Excess Stock</li>
      <li>Manage Product Returns</li>
      <li>Sell Company Assets</li>
    </ul>
    <div class="contact">
      <div class="person-name">Mark <span class="surname">Pellow</span></div>
      <ul class="contact-list">
        <li>
          <svg viewBox="0 0 16 16" aria-hidden="true"><path d="M3 1h3l1.5 4-2 1.2a9 9 0 0 0 4.3 4.3L11 8.5l4 1.5v3a2 2 0 0 1-2 2A13 13 0 0 1 1 3a2 2 0 0 1 2-2z"/></svg>
          027 846 2093
        </li>
        <li>
          <svg viewBox="0 0 16 16" aria-hidden="true"><path d="M1 3h14v10H1z M1 3l7 6 7-6" stroke="#f6f6f4" stroke-width="1"/></svg>
          markpellow@stockharbor.example
        </li>
        <li>
          <svg viewBox="0 0 16 16" aria-hidden="true"><circle cx="8" cy="8" r="7"/></svg>
          www.stockharbor.example
        </li>
      </ul>
    </div>
  </section>

  <section class="card card-back">
    <div class="mascot-art" role="img" aria-label="Cartoon delivery mascot carrying an orange parcel and giving a thumbs up"></div>
    <div class="back-url">www.stockharbor.example</div>
  </section>
</main>
</body>
</html>
```